Corporate PowerPoint Template

Seeking a Powerpoint Template Design for High Technology company based in Silicon Valley. We are seeking a general template design that conveys a professional, clean, progressive message.

The Template must have the following elements at a minimum:
1. Title Page (see comments following)
2. Agenda Page
3. Page Number, Date and Confidentiality Statement
Items in #3 are to appear on all pages except title page

We expect the Title page to be graphical in nature with area for Presentation Title, Presenter Name, Date and a place for confidentiality statement should be present as well. Three (3) distinct Title pages to address different constituencies: Customers, Partners and Internal Communications.

In general, we would like to stay with our corporate color scheme (which may be found in our logo). To better understand our products, logo and look and feel - please visit our website at: http://www.velmarotek.example

```html
<!DOCTYPE html>
<html lang="en">
<head>
<meta charset="utf-8">
<title>Velmarotek Presentation Template</title>
<link rel="stylesheet" href="https://fonts.googleapis.com/css2?family=Questrial&family=Open+Sans:wght@400;600;700&display=swap">
<style>
  :root {
    --page-top: #d8eef8;
    --page-bottom: #eef8fc;
    --brand-blue: #4a7cc9;
    --brand-blue-light: #a9c2e6;
    --brand-teal: #005e63;
    --brand-teal-mid: #0d7b80;
    --header-line: #3b4a4c;
    --row-dark: #cdd7db;
    --row-light: #e6ecec;
    --text-dark: #1d1d1d;
    --text-muted: #8a8f93;
    --white: #ffffff;
    --photo-light: #f7f8f8;
    --photo-mid: #d7dadb;
    --photo-dark: #8e9294;
  }
  * { box-sizing: border-box; margin: 0; padding: 0; }
  html, body { width: 900px; height: 1200px; overflow: hidden; }
  body {
    background: linear-gradient(180deg, var(--page-top), var(--page-bottom));
    font-family: "Questrial", sans-serif;
    position: relative;
  }
  .slide {
    position: absolute;
    left: 103px;
    width: 694px;
    height: 520px;
    background: var(--white);
    box-shadow: 0 2px 6px rgba(0, 40, 60, 0.25);
    overflow: hidden;
  }
  .slide--title { top: 57px; }
  .slide--agenda { top: 613px; background: linear-gradient(180deg, var(--white) 60%, #eef2f6); }

  .title-art { position: absolute; inset: 0; }
  .title-block { position: absolute; left: 24px; top: 80px; color: var(--white); }
  .title-block__title { font-size: 24px; letter-spacing: 0.3px; }
  .title-block__subtitle { font-size: 15px; margin-top: 8px; opacity: 0.92; }

  .brand { position: absolute; display: flex; align-items: center; color: var(--brand-teal); }
  .brand__dot { border-radius: 50%; background: var(--brand-blue); flex: none; }
  .brand--hero { left: 424px; top: 142px; gap: 10px; font-size: 36px; }
  .brand--hero .brand__dot { width: 56px; height: 56px; }
  .brand--footer { left: 14px; top: 482px; gap: 6px; font-size: 17px; }
  .brand--footer .brand__dot { width: 22px; height: 22px; }

  .agenda-header {
    position: absolute; left: 0; top: 0; width: 100%; height: 90px;
    background: linear-gradient(90deg, var(--brand-teal), var(--brand-teal-mid));
    border-bottom: 2px solid var(--header-line);
  }
  .agenda-header__title { position: absolute; left: 42px; top: 37px; font-size: 28px; color: var(--white); }
  .agenda-header__notice {
    position: absolute; right: 14px; top: 12px; font-family: "Open Sans", sans-serif;
    font-size: 10.5px; color: var(--white);
  }
  .header-badge {
    position: absolute; left: 588px; top: 34px; width: 96px; height: 96px;
    border-radius: 50%; background: var(--white);
  }

  .agenda-table {
    position: absolute; left: 40px; top: 133px; width: 625px;
    border-collapse: collapse; font-size: 15.5px; color: var(--text-dark);
  }
  .agenda-table th {
    background: var(--brand-teal); color: var(--white); text-align: left;
    font-family: "Open Sans", sans-serif; font-weight: 700; font-size: 15px;
    height: 26px; padding: 2px 8px 0;
  }
  .agenda-table td { height: 55px; padding: 4px 8px; vertical-align: top; line-height: 1.35; }
  .agenda-table td:first-child, .agenda-table th:first-child { width: 190px; border-right: 1px solid var(--white); }
  .agenda-table tbody tr:nth-child(odd) td { background: var(--row-dark); }
  .agenda-table tbody tr:nth-child(even) td { background: var(--row-light); }

  .slide-footer { position: absolute; top: 487px; font-size: 11px; color: var(--text-muted); }
  .slide-footer--presenter { left: 244px; }
  .slide-footer--date { left: 527px; }
  .slide-footer--page { left: 647px; font-size: 9px; top: 488px; }
</style>
</head>
<body>

<section class="slide slide--title">
  <svg class="title-art" width="694" height="520" viewBox="0 0 694 520">
    <defs>
      <linearGradient id="blueField" x1="0" y1="0" x2="0" y2="1">
        <stop offset="0" stop-color="var(--brand-blue)"/>
        <stop offset="1" stop-color="var(--brand-blue-light)"/>
      </linearGradient>
      <linearGradient id="photoField" x1="0" y1="0" x2="0.3" y2="1">
        <stop offset="0" stop-color="var(--white)"/>
        <stop offset="0.45" stop-color="var(--photo-light)"/>
        <stop offset="0.75" stop-color="var(--photo-mid)"/>
        <stop offset="1" stop-color="var(--photo-dark)"/>
      </linearGradient>
    </defs>
    <polygon points="507,0 694,0 694,520 142,520" fill="url(#photoField)" role="img" aria-label="Photo of a digital caliper measuring a machined part over technical drawings"/>
    <polygon points="0,0 448,0 112,520 0,520" fill="url(#blueField)"/>
    <polygon points="448,0 507,0 142,520 112,520" fill="var(--brand-teal)"/>
  </svg>
  <div class="title-block">
    <h1 class="title-block__title">Presentation Title Text</h1>
    <p class="title-block__subtitle">Presentation Subtitle Text</p>
  </div>
  <div class="brand brand--hero"><span class="brand__dot"></span><span class="brand__name">velmarotek</span></div>
</section>

<section class="slide slide--agenda">
  <header class="agenda-header">
    <h2 class="agenda-header__title">Agenda</h2>
    <p class="agenda-header__notice">Strictly Confidential</p>
  </header>
  <div class="header-badge"></div>

  <table class="agenda-table">
    <thead>
      <tr><th>Agenda</th><th>Description</th></tr>
    </thead>
    <tbody>
      <tr><td>Item 1</td><td>Lorem ipsum dolor sit amet, et pri vide fugit.</td></tr>
      <tr><td>Item 2</td><td>Odio prodesset sea in, indoctum intellegebat in nec, at pri virtute ceteros nominati.</td></tr>
      <tr><td>Item 3</td><td>Mel ea audiam percipit, eum bonorum menandri cotidieque ne.</td></tr>
      <tr><td>Item 4</td><td>Et omnis latine concludaturque cum, his ad wisi assueverit appellantur.</td></tr>
      <tr><td>Item 5</td><td>Mucius option expetendis ei quo, te has elitr ornatus deseruisse.</td></tr>
    </tbody>
  </table>

  <div class="brand brand--footer"><span class="brand__dot"></span><span class="brand__name">velmarotek</span></div>
  <p class="slide-footer slide-footer--presenter">Presenter Name</p>
  <p class="slide-footer slide-footer--date">30 August 2014</p>
  <p class="slide-footer slide-footer--page">2</p>
</section>

</body>
</html>
```